Daily Deals Website Needs a Landing Page (Home Page will act as the landing page)

We need a landing page for a daily deals website that will act as the home page. We have attached the wire frame and logo for reference. Open to creative ideas and suggestions as long as the main elements of the wireframe are incorporated in the design. Need a very simplistic design approach like Vorplex's search page. (www.vorplex.com) . Very clean and distinct CTA's.

Target Market(s)

Customers looking for deals on everyday use items

Font styles to use
Sans Serif

Requirements
Must have
• clean design, lots of white space and strong CTA .
Nice to have
• need a clean design overall. Strong CTA
Should not have
• Cluttered look. Too many colors, keep it simple

```html
<!DOCTYPE html>
<html lang="en">
<head>
<meta charset="utf-8">
<title>DEALVO — Daily Deals</title>
<link rel="stylesheet" href="https://fonts.googleapis.com/css2?family=Poppins:wght@500;600;700&family=Lato:wght@400;700&family=Open+Sans:wght@600;700&display=swap">
<style>
  :root {
    --brand-blue: #1f339a;
    --brand-green: #6cc24a;
    --ink: #1b1b1b;
    --muted: #6f6f6f;
    --field: #f2f3f7;
    --section-tint: #fcfcfc;
    --hero-top: #f8f6f5;
    --white: #ffffff;
  }
  * { box-sizing: border-box; margin: 0; padding: 0; }
  html, body { width: 720px; height: 1200px; overflow: hidden; background: var(--white); }
  body { position: relative; font-family: "Lato", Arial, sans-serif; color: var(--ink); }

  .hero { position: absolute; left: 0; top: 0; width: 720px; height: 269px; text-align: center; }
  .hero-backdrop {
    position: absolute; inset: 0;
    background: linear-gradient(180deg, var(--hero-top) 0%, var(--white) 100%);
  }
  .brand-name {
    position: absolute; left: 0; right: 0; top: 30px;
    font-family: "Poppins", Arial, sans-serif; font-weight: 700; font-size: 32px;
    letter-spacing: 1px; color: var(--brand-blue); line-height: 44px;
  }
  .hero-title {
    position: absolute; left: 0; right: 0; top: 140px;
    font-family: "Poppins", Arial, sans-serif; font-weight: 600; font-size: 33px;
    color: var(--brand-blue); line-height: 44px; letter-spacing: .3px;
  }
  .hero-lead {
    position: absolute; left: 0; right: 0; top: 195px;
    font-size: 9.2px; font-weight: 700; line-height: 11.6px; color: var(--ink);
  }

  .signup-section { position: absolute; left: 0; top: 269px; width: 720px; height: 226px; background: var(--section-tint); }
  .signup-card {
    position: absolute; left: 173px; top: 45px; width: 374px; height: 141px;
    background: var(--white); border-radius: 5px;
    box-shadow: 0 2px 8px rgba(0,0,0,.12); text-align: center;
  }
  .signup-title {
    font-family: "Poppins", Arial, sans-serif; font-weight: 500; font-size: 18px;
    line-height: 24px; margin-top: 21px; color: var(--ink);
  }
  .signup-text { font-size: 8.3px; font-weight: 700; margin-top: 5px; line-height: 11px; }

  .subscribe-form { position: absolute; display: flex; gap: 8px; }
  .signup-card .subscribe-form { left: 48px; top: 86px; }
  .email-field {
    width: 194px; height: 25px; border-radius: 13px; background: var(--field);
    font-size: 9px; font-weight: 700; color: var(--ink); line-height: 25px; padding-left: 9px; text-align: left;
  }
  .cta {
    display: block; height: 25px; border-radius: 13px; background: var(--brand-green);
    color: var(--white); font-size: 8.6px; line-height: 25px; text-align: center;
  }
  .subscribe-form .cta { width: 76px; }

  .deals-title {
    position: absolute; left: 0; right: 0; top: 530px; text-align: center;
    font-family: "Poppins", Arial, sans-serif; font-weight: 600; font-size: 28px;
    line-height: 36px; color: var(--brand-blue); letter-spacing: .5px;
  }
  .deals-lead {
    position: absolute; left: 210px; width: 300px; top: 585px; text-align: center;
    font-size: 8.4px; line-height: 13.7px; color: var(--ink);
  }

  .deal { position: absolute; top: 680px; width: 240px; text-align: center; }
  .deal-featured { left: 94px; }
  .deal-promoted { left: 385px; }
  .deal-label {
    font-family: "Poppins", Arial, sans-serif; font-weight: 600; font-size: 12.6px;
    line-height: 18px; color: var(--brand-blue);
  }
  .deal-photo { display: block; width: 181px; height: 123px; margin: 12px auto 0; border-radius: 2px; }
  .deal-featured .deal-photo { background: linear-gradient(180deg, #dcd8d5 0%, #cdbdb3 100%); }
  .deal-promoted .deal-photo { background: #ececec; }
  .product-name {
    font-family: "Poppins", Arial, sans-serif; font-weight: 600; font-size: 8.4px;
    color: var(--brand-blue); margin-top: 17px; line-height: 12px;
  }
  .product-text { width: 182px; margin: 11px auto 0; font-size: 8.4px; line-height: 13.7px; color: var(--muted); }
  .deal .cta { width: 123px; margin: 9px auto 0; font-size: 9px; }

  .footer { position: absolute; left: 0; top: 1004px; width: 720px; height: 196px; background: var(--brand-blue); color: var(--white); }
  .footer-title {
    position: absolute; left: 0; right: 0; top: 37px; text-align: center;
    font-family: "Poppins", Arial, sans-serif; font-weight: 600; font-size: 18px; line-height: 24px;
  }
  .footer-text { position: absolute; left: 0; right: 0; top: 66px; text-align: center; font-size: 8.3px; font-weight: 700; }
  .footer .subscribe-form { left: 221px; top: 93px; }
  .legal {
    position: absolute; top: 171px; font-family: "Open Sans", Arial, sans-serif;
    font-weight: 700; font-size: 7px; letter-spacing: .3px; line-height: 10px;
  }
  .copyright { left: 56px; }
  .privacy { left: 497px; }
  .terms { left: 585px; }
</style>
</head>
<body>
  <header class="hero">
    <div class="hero-backdrop" role="img" aria-label="Faded lifestyle photo of everyday accessories behind the heading"></div>
    <div class="brand-name">DEALVO</div>
    <h1 class="hero-title">Every deal has a story</h1>
    <p class="hero-lead">Lorem ipsum dolor sit amet, consectetur adipiscing elit, sed do<br>eiusmod tempor incididunt ut labore et dolore magna aliqua.</p>
  </header>

  <section class="signup-section">
    <div class="signup-card">
      <h2 class="signup-title">Sign-up to our mailing list</h2>
      <p class="signup-text">Subscribe to our mailing list, and we'll update you the latest deals.</p>
      <div class="subscribe-form">
        <div class="email-field">Your email</div>
        <span class="cta">Subscribe</span>
      </div>
    </div>
  </section>

  <h2 class="deals-title">Deals Of the day</h2>
  <p class="deals-lead">Lorem ipsum dolor sit amet, consectetur adipiscing elit, sed do eiusmod<br>tempor incididunt ut labore et dolore magna aliqua. Ut enim ad minim veniam,<br>quis nostrud exercitation.</p>

  <article class="deal deal-featured">
    <h3 class="deal-label">Featured Deal of the Day</h3>
    <div class="deal-photo" role="img" aria-label="Product photo of skincare bottles and tubes"></div>
    <h4 class="product-name">Product Name</h4>
    <p class="product-text">Lorem ipsum dolor sit amet, consectetur adipiscing elit, sed do eiusmod tempor incididunt ut labore et dolore magna aliqua.</p>
    <span class="cta">Click to receive deal</span>
  </article>

  <article class="deal deal-promoted">
    <h3 class="deal-label">Promoted Deal of the Day</h3>
    <div class="deal-photo" role="img" aria-label="Product photo of white wireless earbuds"></div>
    <h4 class="product-name">Product Name</h4>
    <p class="product-text">Lorem ipsum dolor sit amet, consectetur adipiscing elit, sed do eiusmod tempor incididunt ut labore et dolore magna aliqua.</p>
    <span class="cta">Click to receive deal</span>
  </article>

  <footer class="footer">
    <h2 class="footer-title">Sign-up to our mailing list</h2>
    <p class="footer-text">Subscribe to our mailing list, and we'll update you the latest deals.</p>
    <div class="subscribe-form">
      <div class="email-field">Your email</div>
      <span class="cta">Subscribe</span>
    </div>
    <span class="legal copyright">Copyright © 2021 DEALVO.&nbsp; All Rights Reserved.</span>
    <span class="legal privacy">Privacy Policy</span>
    <span class="legal terms">Terms of Service</span>
  </footer>
</body>
</html>
```